Redo of existing website www.stonvira.example

I would like it to look like the newer style website, with large images, less text. clean and modern looking. The new design should focus on call to action. ultimately that's what were looking for.Some features I would like to see we try to do good job of keeping up with our blog, and it is a good source of recent pictures of our work. I like four visitors to get the few pieces they're doing with a national brand or franchise pray. I like to stay far from the idea of a local one-man band with magnetic signs on his truck.
I think that clean beautiful images have the biggest impact. In my opinion most people don't read more than a couple lines of text. The text is more for search engines.
we are currently in the process of revising our logo as well, I will upload those files when I get them.
Please feel free to use content and images from our current website www.stonvira.example. we can purchase professional stock images if needed.
1. large call to action with easy contact form.
2. Blog roll on front page to showcase our recent work.
2. All social connect buttons.
Check out our reviews on ratewell!
My current websites
Www.stonvira.example
https://social.example/profile/604918273655102938417/about
www.socialpage.example/stonvira
http://www.blogsite.example/blog/curbguardian
https://microblog.example/Stonvira
websites I like the way they look.
http://quillpost.example/
http://www.cartwell.example/
http://www.brennickpaving.example/
http://www.tarmacways.example/
http://curbandcoatingworks.example/
Hello all,
I have just uploaded some images of our company mascot "Curb Guardian" and our new logo.
Project Deadline Extended
Reason: Death in family. Finally back to work.
Target Market(s)
We have 2 main groups of customers commercial and residential.
Commercial customers are Property owners and managers, operators of multi location business, restaurant, supermarket, banks, and are best source for repeat business
for Residential customers we provide driveway repair and driveway paving services.
for residential customers I would like to encourge the submission or pictures with the inquiry for a quick quote. Residential customers are typically a one time job but are a good source of referrals
I like how this website separates residential and commercial
http://www.glintcoatonline.example
Call

```html
<!DOCTYPE html>
<html lang="en">
<head>
<meta charset="utf-8">
<title>Stonvira — Asphalt Paving</title>
<link href="https://fonts.googleapis.com/css2?family=Montserrat:wght@400;600;700&family=Open+Sans:wght@400;600&family=Roboto+Slab:wght@700&family=Bree+Serif&display=swap" rel="stylesheet">
<style>
:root{
  --green:#1fd11f;
  --green-dark:#1e8a3d;
  --green-deep:#17652c;
  --ink:#1b1b1b;
  --band:#3e3e3e;
  --text:#333;
  --panel:#f3f3f3;
  --line:#dcdcdc;
}
*{margin:0;padding:0;box-sizing:border-box}
html,body{width:742px;height:1200px;overflow:hidden;background:#fff;font-family:'Open Sans',sans-serif;color:var(--text)}
.abs{position:absolute}
.topbar{left:0;top:0;width:742px;height:32px;background:var(--ink)}
.phone{right:62px;top:7px;color:#fff;font:700 14px 'Montserrat',sans-serif;display:flex;align-items:center;gap:8px}
.header{left:0;top:32px;width:742px;height:57px;background:#fff}
.brand{left:61px;top:44px;font:700 21px 'Montserrat',sans-serif;color:var(--green);letter-spacing:1px}
.home{left:296px;top:32px;width:35px;height:57px;background:var(--green);display:flex;align-items:center;justify-content:center}
.nav{left:342px;top:57px;display:flex;gap:13px;font:400 7.5px 'Open Sans',sans-serif;color:#222}
.band{left:0;top:89px;width:742px;height:184px;background:var(--band)}
.hero{left:62px;top:108px;width:614px;height:264px;background:#fff}
.hero-photo{left:66px;top:113px;width:608px;height:254px;background:linear-gradient(180deg,#9fc3e6 0%,#c9dcea 30%,#6f8f4a 45%,#3b3d3e 75%,#2b2c2d 100%)}
.cta{left:272px;top:317px;width:183px;height:39px;border:2px solid var(--green);background:rgba(20,20,20,.85);color:#fff;font:400 16px 'Bree Serif',serif;letter-spacing:1px;display:flex;align-items:center;justify-content:center}
.hero-shadow{left:70px;top:372px;width:598px;height:14px;background:radial-gradient(ellipse at center top,rgba(0,0,0,.35),rgba(0,0,0,0) 70%)}
.intro-title{left:0;top:401px;width:742px;text-align:center;font:600 14px 'Montserrat',sans-serif;letter-spacing:1px;color:#333}
.intro-text{left:0;top:421px;width:742px;text-align:center;font-size:7px;line-height:12.5px;color:#333}
.thumb{top:477px;height:105px}
.thumb .pic{position:absolute;inset:0}
.thumb .cap{position:absolute;left:0;right:0;bottom:0;height:22px;background:rgba(40,110,50,.55);color:#fff;font:400 13px 'Open Sans',sans-serif;padding:1px 7px}
.card{left:62px;width:407px;height:171px;background:var(--panel);border:1px solid #e4e4e4;border-radius:3px}
.tag{width:21px;height:21px;background:var(--green-dark);color:#fff;font:700 7px 'Open Sans',sans-serif;display:flex;align-items:center;justify-content:center}
.card-title{font:400 11px 'Open Sans',sans-serif;color:#333}
.meta{display:flex;gap:16px;font-size:7.5px;color:var(--green-dark)}
.meta span{display:flex;align-items:center;gap:5px}
.dot{width:10px;height:10px;border-radius:50%;background:#444;display:inline-block}
.card-pic{width:100px;height:80px;background:linear-gradient(180deg,#a9b6c2,#e9ecee 55%,#c7a23a 80%,#e6e6e6);border:2px solid #fff;box-shadow:0 1px 3px rgba(0,0,0,.2)}
.card-text{width:265px;font-size:7px;line-height:12.4px;color:#333}
.card-foot{width:388px;border-top:1px solid var(--line);display:flex;align-items:center;font-size:7.5px;padding-top:6px}
.card-foot .ago{color:var(--green-dark)}
.card-foot b{font-weight:600;color:#444}
.sq{width:10px;height:10px;background:#777;display:inline-block;margin-right:8px}
.divider{left:480px;top:606px;height:358px;border-left:1px dashed #ccc}
.contact{left:494px;top:606px;width:185px;height:358px;background:var(--panel);border:1px solid #e4e4e4;border-radius:3px}
.contact-head{left:501px;top:613px;width:174px;height:30px;background:var(--ink);color:#fff;font:400 15px 'Open Sans',sans-serif;padding:4px 9px;border-radius:2px;letter-spacing:.5px}
.contact-text{left:504px;top:649px;width:168px;font-size:8px;line-height:13.5px;text-align:justify;color:#333}
.field{left:502px;width:173px;height:21px;background:#e7e7e7;border:1px solid #cfcfcf;border-radius:2px;font-size:7.5px;padding:6px 8px;color:#333;box-shadow:inset 0 1px 2px rgba(0,0,0,.1)}
.submit{left:612px;top:933px;width:56px;height:16px;background:var(--ink);color:#fff;font:600 7.5px 'Open Sans',sans-serif;display:flex;align-items:center;justify-content:center;border-radius:2px}
.footer{left:0;top:1020px;width:742px;height:180px;background:var(--green-dark)}
.enquiry{left:515px;top:999px;width:158px;height:36px;background:var(--green-deep);color:#fff;font:700 14px 'Roboto Slab',serif;display:flex;align-items:center;justify-content:center;gap:8px;box-shadow:0 2px 4px rgba(0,0,0,.3)}
.col{top:1043px;color:#fff}
.col h3{font:400 13px 'Open Sans',sans-serif;margin-bottom:8px}
.col ul{list-style:none;width:86px}
.col li{font-size:7.5px;padding:4px 0 4px 10px;border-bottom:1px dashed rgba(0,0,0,.25);position:relative}
.col li:before{content:"";position:absolute;left:2px;top:8px;width:3px;height:3px;border-radius:50%;background:rgba(255,255,255,.5)}
.reach{left:441px;top:1043px;color:#fff;font-size:7.5px;line-height:15px}
.reach h3{font:400 13px 'Open Sans',sans-serif;margin-bottom:8px}
.reach .co{font-size:9.5px;margin-bottom:2px}
.bottom{left:62px;top:1160px;width:611px;height:23px;background:#1c3f25;color:#fff;font-size:7.5px;display:flex;align-items:center;padding:0 4px;gap:10px}
.bottom u{margin-left:24px}
.circ{width:15px;height:15px;border-radius:50%;background:#fff;display:inline-block}
</style>
</head>
<body>
<div class="abs topbar"></div>
<div class="abs phone">
  <svg width="17" height="14" viewBox="0 0 17 14"><path d="M1 5c2-3 13-3 15 0l-2 2-3-1V4H6v2L3 7z" fill="var(--green)"/><rect x="4" y="7" width="9" height="6" rx="1" fill="var(--green)"/><circle cx="8.5" cy="10" r="1.6" fill="#1b1b1b"/></svg>
  (555) 014 2290
</div>
<div class="abs header"></div>
<div class="abs brand">STONVIRA</div>
<div class="abs home"><svg width="13" height="11" viewBox="0 0 13 11"><path d="M6.5 0L0 5.5h2V11h3.5V7.5h2V11H11V5.5h2z" fill="#222"/></svg></div>
<nav class="abs nav"><span>COMMERCIAL</span><span>RESIDENTIAL</span><span>ABOUT US</span><span>FREE ESTIMATE</span><span>TESTIMONIALS</span><span>BLOG</span></nav>

<div class="abs band"></div>
<div class="abs hero"></div>
<div class="abs hero-photo" role="img" aria-label="Paving crew in safety vests operating an asphalt paver on a country road"></div>
<div class="abs cta">POST YOUR BLOG</div>
<div class="abs hero-shadow"></div>

<h1 class="abs intro-title">LOREM IPSUM DOLOR ED IT SEDITRED</h1>
<p class="abs intro-text">Based in Alderbrook, Westmere, we design, provide, and service licensed and unlicensed, point-to-point and point-to-multipoint paving systems.<br>For over 25 years, Relayline Systems has built and delivered mission critical surface and resurfacing products</p>

<div class="abs thumb" style="left:62px;width:196px"><div class="pic" role="img" aria-label="Crew laying fresh asphalt beside a building" style="background:linear-gradient(180deg,#8fb4d8,#b89a7a 40%,#2b2b2b 80%)"></div><div class="cap">Lorem Ipsum</div></div>
<div class="abs thumb" style="left:272px;width:196px"><div class="pic" role="img" aria-label="Freshly striped parking lot" style="background:linear-gradient(180deg,#6d7d5a,#3a3a3a 35%,#1f1f1f)"></div><div class="cap">Lorem Ipsum</div></div>
<div class="abs thumb" style="left:481px;width:198px"><div class="pic" role="img" aria-label="Skid steer with snow plow clearing a lot" style="background:linear-gradient(180deg,#b9c3cc,#eceeef 55%,#d4a93a 75%,#e7e7e7)"></div><div class="cap">Lorem Ipsum</div></div>

<div class="abs card" style="top:606px"></div>
<div class="abs tag" style="left:58px;top:612px">Dec</div>
<div class="abs card-title" style="left:87px;top:618px">Starling yaml config file</div>
<div class="abs meta" style="left:76px;top:642px"><span><i class="dot"></i>APRIL 20, 2013</span><span><i class="dot"></i>ADMIN</span><span><i class="dot"></i>0 COMMENTS</span></div>
<div class="abs card-pic" style="left:80px;top:663px" role="img" aria-label="Skid steer plowing snow"></div>
<p class="abs card-text" style="left:193px;top:662px">Welcome! Have a look around but we're still under construction! We'll have a psum has been the industry's standard dummy text ever since full launch soon!<br>In the meantime, please subscribe to one of our social media options in the right column to be notified when the site is finished. simply dummy text of the printing and typesetting industry.</p>
<div class="abs card-foot" style="left:73px;top:752px"><span class="ago">4 hours ago</span>&nbsp;-&nbsp;<b>Like</b><b style="margin:0 18px">Share</b><i class="sq"></i><i class="sq"></i><i class="sq"></i></div>

<div class="abs card" style="top:792px"></div>
<div class="abs tag" style="left:60px;top:798px">Dec</div>
<div class="abs card-title" style="left:88px;top:804px">Starling yaml config file</div>
<div class="abs meta" style="left:77px;top:828px"><span><i class="dot"></i>APRIL 20, 2013</span><span><i class="dot"></i>ADMIN</span><span><i class="dot"></i>0 COMMENTS</span></div>
<div class="abs card-pic" style="left:81px;top:849px" role="img" aria-label="Skid steer plowing snow"></div>
<p class="abs card-text" style="left:194px;top:848px">Welcome! Have a look around but we're still under construction! We'll have a psum has been the industry's standard dummy text ever since full launch soon!<br>In the meantime, please subscribe to one of our social media options in the right column to be notified when the site is finished. simply dummy text of the printing and typesetting industry.</p>
<div class="abs card-foot" style="left:74px;top:938px"><span class="ago">4 hours ago</span>&nbsp;-&nbsp;<b>Like</b><b style="margin:0 18px">Share</b><i class="sq"></i><i class="sq"></i><i class="sq"></i></div>

<div class="abs divider"></div>

<div class="abs contact"></div>
<div class="abs contact-head">Customer Contact</div>
<p class="abs contact-text">Etiam est nunc, venenatis in, tristique eu, imperdiet ac, nisl. Cum sociis natoque penatibus...</p>
<div class="abs field" style="top:696px">Your Name</div>
<div class="abs field" style="top:728px">Email Address</div>
<div class="abs field" style="top:764px">Your Phone</div>
<div class="abs field" style="top:796px">Home Address</div>
<div class="abs field" style="top:832px;height:70px">Your Comments</div>
<div class="abs submit">Submit Now</div>

<div class="abs footer"></div>
<div class="abs enquiry"><svg width="17" height="15" viewBox="0 0 17 15"><rect x="1" y="1" width="15" height="10" fill="none" stroke="#fff" stroke-width="2"/><rect x="6" y="12" width="5" height="2" fill="#fff"/></svg>QUICK ENQUIRY</div>
<div class="abs col" style="left:70px"><h3>Quick Links</h3><ul><li>Home</li><li>Portfolio</li><li>Downloads</li><li>Contact</li></ul></div>
<div class="abs col" style="left:195px"><h3>About</h3><ul><li>Overview</li><li>History</li><li>Staff profiles</li><li>Safety procedures</li></ul></div>
<div class="abs col" style="left:320px"><h3>Services</h3><ul><li>Civil</li><li>Ash fault</li><li>Paving</li><li>Equipment hire</li></ul></div>
<div class="abs reach"><h3>Reach Us</h3><div class="co">Summit Crest Paving</div>Dorian Halloway<br>Mob: 0400-555-017, Office: 5550-12-48<br>Fax: 5550-12-48</div>
<svg class="abs" style="left:592px;top:1070px" width="72" height="62" viewBox="0 0 72 62"><g transform="rotate(-20 36 31)" fill="none" stroke="rgba(255,255,255,.18)" stroke-width="6"><rect x="8" y="14" width="56" height="36"/><path d="M8 14l28 22 28-22"/></g></svg>
<div class="abs bottom">© 2014 &nbsp;All Right reserved &nbsp;|&nbsp; Terms &amp; conditions<u>Privacy Policy</u><span style="margin-left:auto;display:flex;gap:4px"><i class="circ"></i><i class="circ"></i><i class="circ"></i></span></div>
</body>
</html>
```